Tessa's Business Card Design

I am in need of a business card design for our company Holloway Wrecking & Reclaim (WA) Pty Ltd. Apart from being licenced demolition contractors for residential, commercial or industrial projects we have a 20 acre salvage yard full of recycled building materials, we are also licenced to remove Asbestos and we have our own recycling/refuge tip and this site is also licenced to take Asbestos contamination landfill,we also have a sandpit in which we sell sand. Our primary colour is blue and we have a little man logo which i will attach that has been our logo for the good part of the last thirty years so this is to be included, I wont mind if you alter/update him in any way although his tattoo's must remain.
Target Market(s)
Construction & Building Industry
Industry/Entity Type
Industrial
Contact Information for Business Card
HOLLOWAY WRECKING & RECLAIM (WA) PTY LTD
Tessa Holloway
Credit Controller/Payroll Officer
2417 Marlow Ridge Road
UPPER SWAN  WA  6069
PH: 0438 615 207
Fax: (08) 9384 7720
tessa@hwreck.com.au
hollowaywrecking.com.au
Look and feel
Each slider illustrates characteristics of the customer's brand and the style your logo design should communicate.

```html
<!DOCTYPE html>
<html lang="en">
<head>
<meta charset="utf-8">
<title>Holloway Wrecking &amp; Reclaim – Business Card</title>
<link href="https://fonts.googleapis.com/css2?family=Arimo:ital,wght@0,400;0,700;1,400&display=swap" rel="stylesheet">
<style>
  :root {
    --page-bg: #e9e9ea;
    --brand-blue: #2c4aa8;
    --brand-blue-deep: #233d8f;
    --card-white: #ffffff;
    --text-light: #ffffff;
    --accent-lime: #d6e14a;
    --icon-gold: #e2c23a;
    --figure-blue: #4a6cc4;
    --figure-skin: #e7b7b5;
  }
  * { box-sizing: border-box; margin: 0; padding: 0; }
  html, body {
    width: 1200px; height: 900px; overflow: hidden;
    background: var(--page-bg);
    font-family: "Arimo", Arial, sans-serif;
  }
  .canvas { position: relative; width: 1200px; height: 900px; }
  .card {
    position: absolute; left: 320px; width: 560px; height: 320px;
    border-radius: 4px; overflow: hidden;
    box-shadow: 0 6px 18px rgba(0,0,0,0.18);
  }
  /* Back of card */
  .card-back { top: 100px; background: var(--brand-blue); color: var(--text-light); }
  .services { position: absolute; left: 40px; top: 42px; width: 300px; }
  .services-title { font-size: 14px; margin-bottom: 12px; }
  .services-list { list-style: none; font-size: 13px; line-height: 23px; }
  .services-list li::before { content: "•"; margin: 0 10px 0 6px; }
  .mascot-back {
    position: absolute; right: 40px; top: 30px; width: 150px; height: 260px;
    border-radius: 40px;
    background: linear-gradient(180deg, var(--figure-blue) 0%, var(--figure-skin) 70%, var(--brand-blue-deep) 100%);
  }
  /* Front of card */
  .card-front { top: 480px; background: var(--card-white); }
  .front-header { position: absolute; left: 0; top: 0; width: 100%; height: 160px; }
  .mascot-front {
    position: absolute; left: 40px; top: 24px; width: 96px; height: 110px;
    border-radius: 26px;
    background: linear-gradient(180deg, var(--figure-blue) 0%, var(--figure-skin) 75%, var(--icon-gold) 100%);
  }
  .company-name {
    position: absolute; left: 160px; top: 50px; width: 370px;
    color: var(--brand-blue); font-weight: 700;
    font-size: 20px; line-height: 28px; letter-spacing: 1.5px;
  }
  .front-band {
    position: absolute; left: 0; bottom: 0; width: 100%; height: 160px;
    background: var(--brand-blue); color: var(--text-light);
  }
  .person { position: absolute; left: 28px; top: 24px; width: 250px; }
  .person-name { font-size: 17px; font-weight: 700; letter-spacing: 0.5px; }
  .person-role { font-size: 12px; font-style: italic; color: var(--accent-lime); margin: 3px 0 10px; }
  .person-address { font-size: 12px; line-height: 17px; }
  .contact { position: absolute; left: 300px; top: 30px; list-style: none; font-size: 13px; line-height: 24px; }
  .contact li { display: flex; align-items: center; gap: 10px; }
  .contact svg { width: 14px; height: 14px; flex: none; }
</style>
</head>
<body>
<main class="canvas">
  <section class="card card-back" aria-label="Card back">
    <div class="services">
      <p class="services-title">Our Services Include :</p>
      <ul class="services-list">
        <li>Demolition &amp; Salvage</li>
        <li>Asbestos removal and clean up</li>
        <li>Site clearing/rear lots</li>
        <li>Subdivisional clearing</li>
        <li>Tree and vegetation removal</li>
        <li>Crushing and screening</li>
        <li>Emergency call outs</li>
        <li>Recycling all concrete and brick materials</li>
      </ul>
    </div>
    <div class="mascot-back" role="img" aria-label="Cartoon mascot: a tattooed worker in a hard hat swinging a sledgehammer"></div>
  </section>

  <section class="card card-front" aria-label="Card front">
    <div class="front-header">
      <div class="mascot-front" role="img" aria-label="Cartoon mascot: a worker in a hard hat swinging a sledgehammer"></div>
      <p class="company-name">HOLLOWAY WRECKING &amp; RECLAIM (WA) PTY LTD</p>
    </div>
    <div class="front-band">
      <div class="person">
        <p class="person-name">TESSA HOLLOWAY</p>
        <p class="person-role">Credit Controller/Payroll Officer</p>
        <p class="person-address">2417 Marlow Ridge Road<br>Carrow Heights WA 6071</p>
      </div>
      <ul class="contact">
        <li><svg viewBox="0 0 16 16" aria-hidden="true"><path fill="#e2c23a" d="M2 5c0-2 2-3 6-3s6 1 6 3l-3 1-1-2H6L5 6zM3 7h10l1 7H2z"/></svg>0438 615 207</li>
        <li><svg viewBox="0 0 16 16" aria-hidden="true"><rect x="2" y="5" width="12" height="8" rx="1" fill="#e2c23a"/><rect x="4" y="2" width="8" height="4" fill="#e2c23a"/></svg>(08) 9384 7720</li>
        <li><svg viewBox="0 0 16 16" aria-hidden="true"><rect x="1" y="3" width="14" height="10" rx="1" fill="#e2c23a"/><path d="M1 4l7 5 7-5" stroke="#2c4aa8" stroke-width="1.2" fill="none"/></svg>tessa@hwreck.com.au</li>
        <li><svg viewBox="0 0 16 16" aria-hidden="true"><circle cx="8" cy="8" r="6.5" fill="none" stroke="#e2c23a" stroke-width="1.5"/><path d="M1.5 8h13M8 1.5c3 3 3 10 0 13M8 1.5c-3 3-3 10 0 13" stroke="#e2c23a" stroke-width="1.2" fill="none"/></svg>www.hollowaywrecking.com.au</li>
      </ul>
    </div>
  </section>
</main>
</body>
</html>
```